Tri-Fold Brochure Redesign for Floral Preservation Business

I would like to redesign my current tri-fold brouchue that I created myself and have it updated. I would like to keep the same content, color and images, but have it redesigned to look fresher and updated. I'm in the the floral preservation business and work with brides in the wedding inductry. I'm looking for a royal/rustic feel and it should relate to the look and feel of my website www.larkmeadow.com. I have included the Photoshop file I used to create my orginal bouchure.

The only content that has changed is my address which is now;
2847 Birchfall Court, Reston VA 20173

Safe Zone Width - 10.875
Safe Zone Height - 8.375

I have included the Photoshop and Illustrator templates for the tri-fold brochure from the printer I will be using.

```html
<!DOCTYPE html>
<html lang="en">
<head>
<meta charset="utf-8">
<title>Lark Meadow – Tri-Fold Brochure</title>
<link rel="stylesheet" href="https://fonts.googleapis.com/css2?family=Cinzel:wght@600;700&family=Raleway:wght@400;800&family=Lato:wght@400;700&family=Pinyon+Script&display=swap">
<style>
  :root {
    --crimson: #b51f38;
    --crimson-dark: #8f1529;
    --slate: #6f7073;
    --paper: #f4f2ee;
    --paper-edge: #e6e1da;
    --ink: #3a3a3a;
    --white: #ffffff;
    --gold: #b89a5e;
    --frame-wood: #4a1e1a;
    --mat: #efece6;
  }
  * { margin: 0; padding: 0; box-sizing: border-box; }
  html, body { width: 1200px; height: 800px; overflow: hidden; background: #dcdcdc; }
  .brochure {
    position: relative; width: 1200px; height: 800px;
    background: radial-gradient(ellipse at 50% 30%, var(--paper) 0%, var(--paper-edge) 100%);
    font-family: "Lato", sans-serif; color: var(--ink);
  }
  .band-art { position: absolute; left: 0; top: 0; width: 1200px; height: 800px; }
  .fold { position: absolute; top: 0; width: 1px; height: 800px; background: rgba(0,0,0,0.08); }
  .panel { position: absolute; top: 0; width: 400px; height: 800px; }
  .panel--presentation { left: 0; }
  .panel--jewelry { left: 400px; }
  .panel--contact { left: 800px; }

  .shadowbox {
    position: absolute; left: 68px; top: 56px; width: 264px; height: 270px;
    border: 14px solid var(--frame-wood); background: var(--mat);
    box-shadow: 0 4px 10px rgba(0,0,0,0.25);
  }
  .shadowbox .photo { position: absolute; inset: 22px; background: radial-gradient(circle, #f3efe2 0%, #d9d4c4 60%, #c9c3b2 100%); }
  .feature-photo {
    position: absolute; left: 40px; top: 40px; width: 320px; height: 240px;
    border: 8px solid var(--crimson); outline: 1px solid var(--gold); outline-offset: 4px;
    background: radial-gradient(ellipse at 50% 55%, #9da0a8 0%, #d8d9dc 45%, #ecebea 100%);
  }
  .thumb { position: absolute; top: 36px; width: 140px; height: 120px; border: 4px solid var(--white); box-shadow: 0 2px 6px rgba(0,0,0,0.2); }
  .thumb--bouquet { left: 50px; background: radial-gradient(circle, #d6b25a 0%, #8a6a3a 55%, #2b2420 100%); }
  .thumb--bracelet { left: 210px; background: radial-gradient(ellipse, #5fb7d8 0%, #c7dde6 55%, #f2f2f2 100%); }

  .heading {
    position: absolute; left: 30px; font-family: "Cinzel", serif; font-weight: 700;
    color: var(--crimson); font-size: 20px; letter-spacing: 0.5px; text-transform: uppercase;
  }
  .heading-rule { position: absolute; left: 30px; width: 70px; height: 4px; border-top: 1px solid var(--gold); border-bottom: 1px solid var(--gold); }
  .panel--presentation .heading { top: 350px; }
  .panel--presentation .heading-rule { top: 378px; }
  .panel--jewelry .heading { top: 302px; }
  .panel--jewelry .heading-rule { top: 330px; }
  .body-copy { position: absolute; left: 30px; width: 340px; font-size: 11.5px; line-height: 1.45; text-align: justify; }
  .panel--presentation .body-copy { top: 390px; }
  .panel--jewelry .body-copy { top: 342px; }

  .process-title {
    position: absolute; left: 30px; top: 564px; font-family: "Cinzel", serif;
    font-weight: 700; font-size: 19px; color: var(--white); letter-spacing: 1px;
  }
  .step { position: absolute; display: flex; gap: 16px; color: var(--white); }
  .step-label {
    width: 92px; flex: none; text-align: center; font-family: "Raleway", sans-serif;
    font-size: 13px; line-height: 1.25; text-transform: uppercase; letter-spacing: 0.5px;
  }
  .step-label strong { display: block; font-family: "Cinzel", serif; font-weight: 700; font-size: 14px; }
  .step-copy { font-size: 11px; line-height: 1.45; text-align: justify; }
  .panel--presentation .step { left: 20px; top: 622px; width: 360px; }
  .panel--jewelry .step { left: 20px; top: 585px; width: 360px; }
  .panel--contact .step { left: 20px; top: 522px; width: 360px; }

  .quote {
    position: absolute; left: 70px; top: 186px; width: 260px; text-align: center;
    font-family: "Pinyon Script", cursive; font-size: 21px; line-height: 1.35; color: var(--crimson);
  }
  .quote-mark { position: absolute; font-family: "Cinzel", serif; font-weight: 700; font-size: 40px; color: var(--crimson); }
  .quote-mark--open { left: 40px; top: 176px; }
  .quote-mark--close { left: 338px; top: 318px; }
  .visit { position: absolute; left: 70px; top: 370px; width: 260px; text-align: center; font-size: 11px; line-height: 1.4; }
  .visit-web { display: block; margin-top: 3px; font-weight: 700; color: var(--crimson); }
  .visit-address { display: flex; justify-content: center; align-items: center; gap: 5px; }
  .visit-address svg { width: 9px; height: 12px; flex: none; }
</style>
</head>
<body>
<main class="brochure">
  <svg class="band-art" viewBox="0 0 1200 800" aria-hidden="true">
    <path fill="var(--slate)" d="M0 552 H330 C420 552 440 530 540 530 H760 C860 530 880 466 980 466 H1200 V800 H0 Z"/>
    <path fill="var(--crimson)" d="M0 600 H330 C420 600 440 548 540 548 H760 C860 548 880 484 980 484 H1200 V800 H0 Z"/>
    <path fill="none" stroke="var(--gold)" stroke-width="1" d="M0 604 H330 C420 604 440 552 540 552 H760 C860 552 880 488 980 488 H1200"/>
  </svg>
  <div class="fold" style="left:400px"></div>
  <div class="fold" style="left:800px"></div>

  <section class="panel panel--presentation">
    <div class="shadowbox"><div class="photo" role="img" aria-label="Preserved white bridal bouquet mounted in a shadowbox"></div></div>
    <h2 class="heading">Floral Presentation</h2>
    <div class="heading-rule"></div>
    <p class="body-copy">Our handcrafted shadowboxes are made with the industry's finest raw materials to ensure the highest level of quality. We exclusively use Harlow Vance mouldings, makers of beautiful moulding for over 100 years. Using archival standards set by the National Paper Conservancy, our shadowboxes are matted and mounted with the Ashcombe Archival system used to protect some of this nation's most valuable artwork. We finish by using ClearHaven museum glass to enhance, protect and beautify. Each of these details contributes to a museum-quality work of art.</p>
    <h3 class="process-title">THE PROCESS</h3>
    <div class="step">
      <div class="step-label"><strong>Step 1</strong>Reserve the Date</div>
      <p class="step-copy">To ensure our services, you will need to "reserve the date" with a deposit. We accept no more than a set number of clients each week. With over 50,000 weddings in the DC and Tidewater areas annually, many brides reserve their wedding date 10 to 6 months in advance. The full deposit is applied to the cost of your final design selection.</p>
    </div>
  </section>

  <section class="panel panel--jewelry">
    <div class="feature-photo" role="img" aria-label="Silver bracelet with handmade flower-petal beads"></div>
    <h2 class="heading">Flower-Petal Jewelry</h2>
    <div class="heading-rule"></div>
    <p class="body-copy">If you would like to turn your memories into a wearable story, consider creating signature jewelry. We turn real petals from your blooms into one-of-a-kind jewelry pieces for you or your loved ones. We can transform your flowers into earrings, necklaces, bracelets, pendants and Italian-style charms or rosaries. The tradition hails from the historical practice of nuns creating rosaries from condensed flower petals. In that same spirit, we create unique pieces to fit your own style. Each bead is made by hand from your flowers and the highest quality sterling silver findings.</p>
    <div class="step">
      <div class="step-label"><strong>Step 2</strong>Secure the Flower</div>
      <p class="step-copy">You can either drop your flowers off shortly after the event, or we can pick them up the night of. If your event is out of town, no problem. You can ship them to us overnight or drop them off upon your return.</p>
    </div>
  </section>

  <section class="panel panel--contact">
    <div class="thumb thumb--bouquet" role="img" aria-label="Preserved colourful bouquet in a frame"></div>
    <div class="thumb thumb--bracelet" role="img" aria-label="Blue flower-petal bead bracelet"></div>
    <span class="quote-mark quote-mark--open">&ldquo;</span>
    <p class="quote">You have chosen the perfect flowers, now choose the perfect way to cherish them. Lark Meadow's floral preservation process transforms your flowers into lasting works of art or jewelry</p>
    <span class="quote-mark quote-mark--close">&rdquo;</span>
    <p class="visit">Please visit our website for full details, pricing and additional pictures.
      <span class="visit-web">www.larkmeadow.com</span>
      <span class="visit-address"><svg viewBox="0 0 9 12" aria-hidden="true"><path fill="var(--crimson)" d="M4.5 0A4.5 4.5 0 0 0 0 4.5C0 8 4.5 12 4.5 12S9 8 9 4.5A4.5 4.5 0 0 0 4.5 0Zm0 6.2a1.7 1.7 0 1 1 0-3.4 1.7 1.7 0 0 1 0 3.4Z"/></svg>2847 Birchfall Court, Reston VA 20173</span>
    </p>
    <div class="step">
      <div class="step-label"><strong>Step 3</strong>Design Selection</div>
      <p class="step-copy">Within 30 days after your event, we ask that you make an appointment to visit our studio to make your final design selection. Once your order has been placed, it takes approximately 1 to 3 months to complete.</p>
    </div>
  </section>
</main>
</body>
</html>
```